Business Card for Ferncliff Massage

I need a business card for my massage therapy & cannabis oil practice. I already have a logo,the "massage" got edited out of this file. I will send the original soon. I need these elements to be on the card:
web: FerncliffMassage.example
ph: 417/283-9061
email: Mirela.Dawkant@mailbox.example
Other slogans, statements to consider:
Science Geek, Massage Therapist, Neuromuscular Therapy, Cannabis Spa Treatments, Raindrop Therapy, Essential Oils
Target Market(s)
women between 20 & 65, people with enough $ to afford regular massage, people who recently had a motor vehicle accident, Halvora HMP insured
Industry/Entity Type
Massage Therapy
Contact Information for Business Card
I would like to see my bear logo featured; contact details, greens & blues preferred colors.

```html
<!DOCTYPE html>
<html lang="en">
<head>
<meta charset="utf-8">
<title>Ferncliff Massage – Business Card</title>
<link rel="stylesheet" href="https://fonts.googleapis.com/css2?family=Almendra&family=Tinos&display=swap">
<style>
  :root {
    --page: #ecebe8;
    --card: #ffffff;
    --green: #2f7d3a;
    --stone: #8a7b72;
    --stone-dark: #6f6660;
    --ink: #2a2a2a;
    --rule: #9a9a9a;
  }
  * { box-sizing: border-box; margin: 0; padding: 0; }
  html, body { width: 1200px; height: 1200px; overflow: hidden; }
  body {
    background: var(--page);
    position: relative;
    font-family: "Tinos", serif;
    color: var(--ink);
  }
  .card {
    position: absolute;
    left: 150px;
    width: 900px;
    height: 514px;
    background: var(--card);
    box-shadow: 0 6px 18px rgba(0,0,0,0.15);
    overflow: hidden;
  }
  .card--front { top: 50px; border-top: 10px solid var(--green); }
  .card--back { top: 630px; }

  .front__band {
    position: absolute;
    left: 0; right: 0; bottom: 0;
    height: 120px;
    background: var(--green);
  }
  .front__logo-art {
    position: absolute;
    left: 50px; bottom: 110px;
    width: 230px; height: 120px;
    border-radius: 60px 60px 20px 20px;
    background: linear-gradient(135deg, var(--stone) 0%, var(--stone-dark) 100%);
  }
  .front__wordmark {
    position: absolute;
    left: 60px; bottom: 36px;
    font-family: "Tinos", serif;
    font-size: 58px;
    color: #ffffff;
    letter-spacing: 1px;
  }
  .front__name {
    position: absolute;
    left: 330px; bottom: 150px;
    font-family: "Almendra", serif;
    font-size: 42px;
    color: var(--green);
  }
  .front__rule {
    position: absolute;
    left: 330px; right: 40px; top: 40px;
    height: 1px; background: var(--rule);
  }
  .contact {
    position: absolute;
    right: 40px; top: 70px;
    list-style: none;
    text-align: right;
  }
  .contact__item {
    display: flex;
    align-items: center;
    justify-content: flex-end;
    gap: 14px;
    font-size: 25px;
    line-height: 1;
    margin-bottom: 20px;
  }
  .contact__icon { width: 24px; height: 24px; flex: none; }

  .back__logo-art {
    position: absolute;
    left: 330px; top: 60px;
    width: 260px; height: 170px;
    border-radius: 80px 80px 30px 30px;
    background: linear-gradient(135deg, var(--stone) 0%, var(--stone-dark) 70%, var(--green) 100%);
  }
  .back__wordmark {
    position: absolute;
    left: 0; right: 0; top: 250px;
    text-align: center;
    font-family: "Tinos", serif;
    font-size: 66px;
    color: var(--stone-dark);
    letter-spacing: 1px;
  }
  .back__services {
    position: absolute;
    left: 0; right: 0; top: 360px;
    text-align: center;
    font-size: 25px;
    line-height: 1.45;
    font-style: italic;
    color: var(--ink);
  }
</style>
</head>
<body>

<section class="card card--front" aria-label="Card front">
  <div class="front__band"></div>
  <div class="front__logo-art" role="img" aria-label="Ferncliff bear and stacked stones logo mark"></div>
  <div class="front__wordmark">Ferncliff</div>
  <div class="front__name">Mirela Dawkant</div>
  <div class="front__rule"></div>
  <ul class="contact">
    <li class="contact__item">417/283-9061
      <svg class="contact__icon" viewBox="0 0 24 24" aria-hidden="true"><rect width="24" height="24" fill="#2f7d3a"/><path d="M8 5l3 3-2 2a9 9 0 0 0 5 5l2-2 3 3-2 3C10 19 5 14 5 7z" fill="#fff"/></svg>
    </li>
    <li class="contact__item">FerncliffMassage.example
      <svg class="contact__icon" viewBox="0 0 24 24" aria-hidden="true"><rect width="24" height="24" fill="#2f7d3a"/><circle cx="12" cy="12" r="7" fill="none" stroke="#fff" stroke-width="1.6"/><path d="M5 12h14M12 5c-4 4-4 10 0 14M12 5c4 4 4 10 0 14" fill="none" stroke="#fff" stroke-width="1.4"/></svg>
    </li>
    <li class="contact__item">Mirela.Dawkant@mailbox.example
      <svg class="contact__icon" viewBox="0 0 24 24" aria-hidden="true"><rect width="24" height="24" fill="#2f7d3a"/><rect x="5" y="7" width="14" height="10" fill="none" stroke="#fff" stroke-width="1.6"/><path d="M5 7l7 6 7-6" fill="none" stroke="#fff" stroke-width="1.6"/></svg>
    </li>
    <li class="contact__item">2740 NE Larkspur Ave Millbrook, OR, 97000
      <svg class="contact__icon" viewBox="0 0 24 24" aria-hidden="true"><rect width="24" height="24" fill="#2f7d3a"/><path d="M12 20s-6-6-6-10a6 6 0 0 1 12 0c0 4-6 10-6 10z" fill="#fff"/><circle cx="12" cy="10" r="2.2" fill="#2f7d3a"/></svg>
    </li>
  </ul>
</section>

<section class="card card--back" aria-label="Card back">
  <div class="back__logo-art" role="img" aria-label="Ferncliff bear and stacked stones logo mark"></div>
  <div class="back__wordmark">Ferncliff</div>
  <p class="back__services">Science Geek, Massage Therapist, Neuromuscular Therapy, Cannabis Spa<br>Treatments, Raindrop Therapy, Essential Oils</p>
</section>

</body>
</html>
```